Marketing Brochure design required by Video Production company

We are looking for a slick, professional and eye-catching design for a marketing brochure that will showcase our company and its services.

Purpose:
The purpose of the brochure is to show our company as experienced, capable, professional and creative.

The Brochure:
The brochure will be 10 pages (including front and back cover), designed for printing in measurements of 16cm (height) x 18cm (wide).

Attached you will find:

1. Brochure Copy/Text - this is all the text to be included in the brochure. Text in red colour is not to be included in the design but is there as a guide to assist in the design

2. Design assets - our logo and hi-resolution images to be included in the design. The filenames of the images correspond with pages in the Brochure Copy/Text (as you will see)
* this does not seem to be attaching here in ArtMarketHub. Please download this file from stashbin here: https://www.stashbin.net/s/qk4tr7wnz2lpa0e/Product_Marketing_Brochure_Assets-2016-02-07.zip?dl=0

Design:
We would like the design to be open - not cramped or squashed in. Use of space is good. We want it to look very professional, but creative. And also feel simple and easy to read.

Colours to use - blues with black & white (black & white is our brand).

Please feel free to ask any questions you might have.

Thank you.

Industry/Entity Type

It Company

Font styles to use
Sans Serif

Colors
0592cd
3176b5
3276b5
33a6d7
85cae6
cee9f5
85acd3
eaf1f7

Requirements
Must have
• As per the description.
• Download design assets from:
• https://www.stashbin.net/s/qk4tr7wnz2lpa0e/Product_Marketing_Brochure_Assets-2016-02-07.zip?dl=0

```html
<!DOCTYPE html>
<html lang="en">
<head>
<meta charset="utf-8">
<title>Video Production Brochure – Your Story / Your Event Spread</title>
<link href="https://fonts.googleapis.com/css2?family=Michroma&family=Didact+Gothic&display=swap" rel="stylesheet">
<style>
  :root {
    --backdrop: #6f7082;
    --backdrop-light: #8a8b9c;
    --page: #eeeeef;
    --page-edge: #dcdcde;
    --ink: #1e1e22;
    --ink-soft: #3a3a40;
    --band: #bdbdc0;
    --block-grey: #d2d2d5;
    --photo-warm: #b7a79a;
    --photo-cool: #8f98a8;
    --photo-skin: #c9a48c;
    --photo-dark: #4e4a50;
    --event-deep: #5a4a7c;
    --event-mid: #8a78a8;
    --event-light: #b3a6c8;
    --heading-light: rgba(255, 255, 255, 0.85);
  }
  * { box-sizing: border-box; margin: 0; padding: 0; }
  html, body { width: 1200px; height: 1000px; overflow: hidden; }
  body {
    background: radial-gradient(ellipse at 50% 40%, var(--backdrop-light), var(--backdrop));
    font-family: "Didact Gothic", Arial, sans-serif;
    color: var(--ink);
    position: relative;
  }
  .spread {
    position: absolute;
    left: 50px; top: 190px;
    width: 1100px; height: 620px;
    display: flex;
    box-shadow: 0 18px 40px rgba(0,0,0,0.35);
  }
  .page {
    position: relative;
    width: 550px; height: 620px;
    background: var(--page);
    overflow: hidden;
  }
  .page--left { border-right: 1px solid var(--page-edge); }
  .page-art { position: absolute; left: 0; top: 0; }

  .page-title {
    position: absolute;
    font-family: "Michroma", "Arial Black", sans-serif;
    font-size: 44px;
    letter-spacing: 2px;
    line-height: 1;
    white-space: nowrap;
  }
  .page-title--story { left: 92px; top: 188px; color: var(--ink); }
  .page-title--event { left: 30px; top: 205px; color: var(--heading-light); }

  .copy {
    position: absolute;
    font-size: 12.5px;
    line-height: 1.32;
    font-variant: small-caps;
    color: var(--ink-soft);
  }
  .copy p { margin-bottom: 6px; }
  .copy ul { list-style: none; }
  .copy li { padding-left: 6px; }
  .copy li::before { content: "- "; }
  .copy h2 {
    font-family: "Didact Gothic", Arial, sans-serif;
    font-weight: 400;
    font-size: 16px;
    font-variant: small-caps;
    color: var(--ink);
    margin-bottom: 3px;
  }
  .copy--story-intro { left: 34px; top: 380px; width: 262px; text-align: center; }
  .copy--story-package { left: 316px; top: 282px; width: 214px; }
  .copy--event-intro { left: 30px; top: 268px; width: 236px; }
  .copy--event-package { left: 300px; top: 268px; width: 230px; }
  .copy .lead { font-size: 13px; color: var(--ink); }

  .quote-band {
    position: absolute;
    background: var(--band);
    font-size: 13px;
    font-variant: small-caps;
    line-height: 1.35;
    color: var(--ink);
    text-align: right;
    padding: 12px 18px;
  }
  .quote-band--story { left: 300px; top: 500px; width: 250px; height: 64px; }
  .quote-band--event { left: 250px; top: 470px; width: 300px; height: 60px; }
</style>
</head>
<body>
  <main class="spread">
    <section class="page page--left">
      <svg class="page-art" width="550" height="620" viewBox="0 0 550 620">
        <defs>
          <linearGradient id="story-photo-a" x1="0" y1="0" x2="1" y2="1">
            <stop offset="0" stop-color="#d8d2cc"/><stop offset="1" stop-color="#a99c90"/>
          </linearGradient>
          <linearGradient id="story-photo-b" x1="0" y1="0" x2="1" y2="1">
            <stop offset="0" stop-color="#9fa6b6"/><stop offset="1" stop-color="#d9cfc3"/>
          </linearGradient>
          <linearGradient id="story-photo-c" x1="0" y1="0" x2="1" y2="1">
            <stop offset="0" stop-color="#c8a58e"/><stop offset="1" stop-color="#7d6a62"/>
          </linearGradient>
        </defs>
        <rect x="0" y="22" width="120" height="108" fill="url(#story-photo-a)" role="img" aria-label="Photo: smiling man in an office"/>
        <rect x="0" y="135" width="120" height="112" fill="#8d8580" role="img" aria-label="Photo: team member at work"/>
        <rect x="0" y="252" width="120" height="108" fill="#5e5654" role="img" aria-label="Photo: man speaking to camera"/>
        <rect x="125" y="0" width="170" height="112" fill="url(#story-photo-b)" role="img" aria-label="Photo: newspaper and office backdrop"/>
        <rect x="300" y="0" width="140" height="92" fill="#a39a94" role="img" aria-label="Photo: woman with glasses"/>
        <rect x="300" y="98" width="122" height="134" fill="url(#story-photo-c)" role="img" aria-label="Photo: woman being interviewed"/>
        <circle cx="300" cy="560" r="330" fill="var(--page)"/>
      </svg>

      <h1 class="page-title page-title--story">YOUR STORY</h1>

      <div class="copy copy--story-intro">
        <p>The Your Story video profile is a combination of interviews and overlay footage designed to tell your business' story. This style of video content helps your audience better understand:</p>
        <p>- What makes you unique<br>- Why they should trust you<br>- What your product offering is and how it works<br>- What your process is</p>
        <p>We'll work with you to develop the best approach to deliver this in a sharp &amp; engaging fashion.</p>
      </div>

      <div class="copy copy--story-package">
        <h2>The package includes:</h2>
        <ul>
          <li>Filming of interviews + overlay footage at your desired location</li>
          <li>A slick, professionally edited high definition video</li>
          <li>Quick turnaround time and review process</li>
          <li>An opportunity to make any changes before your video is finalised</li>
          <li>Delivery in your choice of formats</li>
        </ul>
      </div>

      <div class="quote-band quote-band--story">Have additional requirements? No problem.<br>Contact us to discuss a quote.</div>
    </section>

    <section class="page page--right">
      <svg class="page-art" width="550" height="620" viewBox="0 0 550 620">
        <defs>
          <radialGradient id="event-photo" cx="0.55" cy="0.55" r="0.7">
            <stop offset="0" stop-color="var(--event-light)"/>
            <stop offset="0.5" stop-color="var(--event-mid)"/>
            <stop offset="1" stop-color="var(--event-deep)"/>
          </radialGradient>
        </defs>
        <rect x="0" y="0" width="130" height="120" fill="var(--block-grey)"/>
        <circle cx="270" cy="40" r="212" fill="url(#event-photo)" role="img" aria-label="Photo: guests on stage at a launch event, purple lighting"/>
      </svg>

      <h1 class="page-title page-title--event">YOUR EVENT</h1>

      <div class="copy copy--event-intro">
        <p class="lead">Event Coverage &amp; Highlights</p>
        <p>Got a launch, seminar, celebration, party or any other event that you want filmed? We've got you covered.</p>
        <p>The Your Event package provides creative event coverage, with the best parts of your event condensed into a slick highlights video that captures the vibe and essence of your event.</p>
      </div>

      <div class="copy copy--event-package">
        <h2>The package includes:</h2>
        <ul>
          <li>Filming of your event exactly as you need</li>
          <li>A slick, professionally edited high definition video, cut to music to suit your event</li>
          <li>An opportunity to review an edit and make changes before your video is finalised</li>
          <li>Delivery in your choice of formats</li>
          <li>Speech &amp; speaker recording also available</li>
        </ul>
      </div>

      <div class="quote-band quote-band--event">Have additional requirements? No problem.<br>Contact us to discuss a quote.</div>
    </section>
  </main>
</body>
</html>
```